Fleeing Marisol Bay website

A very basic website using the graphics provided. The site would give the user the ability to read a description of the book, read testimonials, About the author, Read chapter 1, link to vantoro, order direct via quidlet.

```html
<!DOCTYPE html>
<html lang="en">
<head>
<meta charset="utf-8">
<title>Fleeing Marisol Bay</title>
<link href="https://fonts.googleapis.com/css2?family=Cinzel:wght@400;700&family=Open+Sans:ital,wght@0,300;0,400;0,600;1,300&display=swap" rel="stylesheet">
<style>
:root{
  --ink-black:#000;
  --paper:#efece4;
  --topbar:#cdc8bb;
  --accent:#d9761b;
  --text:#6b6b6b;
  --text-dark:#3d3d3d;
  --frame:#ddd6cc;
  --frame-edge:#c9c0b3;
  --rule:#c9c4b9;
  --buy-red:#b5433e;
  --order-orange:#f4a93c;
  --star-on:#f08a00;
  --star-off:#8e8e8e;
  --btn-top:#ffb21c;
  --btn-bottom:#f49400;
  --title-gold:#f6c52a;
  --title-cream:#f3e8c8;
}
*{box-sizing:border-box;margin:0;padding:0}
html,body{width:1200px;height:800px;overflow:hidden;background:var(--ink-black)}
body{position:relative;font-family:"Open Sans",sans-serif}

/* Left cover side */
.cover-side{position:absolute;left:0;top:0;width:585px;height:800px;background:var(--ink-black)}
.book-cover{position:absolute;left:115px;top:69px;width:425px;height:655px;overflow:hidden}
.cover-band{position:absolute;left:0;top:0;width:100%;height:150px;
  background:radial-gradient(ellipse at 50% 40%,#5a1f1f 0%,#3b1212 55%,#1c0808 100%)}
.cover-art{position:absolute;left:0;top:148px;width:100%;height:507px;
  background:linear-gradient(180deg,#6e7a84 0%,#7fa6bf 18%,#5c7c5a 45%,#2a2a22 70%,#050505 100%)}
.cover-title{position:absolute;left:0;top:36px;width:100%;text-align:center;font-family:"Cinzel",serif;line-height:1}
.cover-title .line-one{display:block;font-size:34px;color:var(--title-cream);letter-spacing:1px}
.cover-title .line-two{display:block;font-size:44px;color:var(--title-gold);margin-top:13px;letter-spacing:0}
.cover-author{position:absolute;left:0;top:571px;width:100%;text-align:center;font-family:"Cinzel",serif;
  font-size:33px;font-weight:700;color:#d8d8d8;letter-spacing:1px}

/* Right info side */
.info-side{position:absolute;left:586px;top:0;width:614px;height:800px;background:var(--paper);overflow:hidden}
.top-bar{position:absolute;left:0;top:0;width:100%;height:57px;background:var(--topbar);border-bottom:1px solid #b9b3a6}
.shop-link{position:absolute;top:2px;width:67px;height:55px;background:#f9f8f5;text-decoration:none}
.shop-link .label{display:block;height:17px;line-height:17px;font-size:9px;color:#fff;text-align:center}
.shop-link .name{display:block;line-height:37px;text-align:center;font-size:13px;font-weight:600;color:#1e3f7a}
.shop-vantoro{left:333px}
.shop-vantoro .label{background:var(--buy-red)}
.shop-vantoro .name{color:#222}
.shop-quidlet{left:401px}
.shop-quidlet .label{background:var(--order-orange)}

.photo-frame{position:absolute;width:173px;height:173px;background:var(--frame);border:1px solid var(--frame-edge);padding:8px}
.photo-frame .fill{width:100%;height:100%}
.author-frame{left:40px;top:75px}
.author-frame .fill{background:linear-gradient(160deg,#8a8a8a 0%,#5e5e5e 50%,#1d1d1d 100%)}
.book-frame{left:40px;top:333px}
.book-frame .fill{background:linear-gradient(135deg,#f7f6f2 0%,#e9e6df 40%,#3a2a22 60%,#171717 100%)}

.section-title{position:absolute;font-family:"Cinzel",serif;font-weight:700;font-size:16px;color:var(--accent);letter-spacing:0.5px}
.section-text{position:absolute;width:272px;font-size:11px;font-weight:300;line-height:16.3px;color:var(--text)}
.about-title{left:225px;top:91px}
.about-text{left:225px;top:126px}
.desc-title{left:225px;top:348px}
.desc-text{left:225px;top:382px}

.rule{position:absolute;left:108px;width:330px;height:1px;background:var(--rule)}
.rule-one{top:300px}
.rule-two{top:597px}

.read-button{position:absolute;left:225px;top:535px;width:128px;height:38px;border-radius:3px;
  background:linear-gradient(var(--btn-top),var(--btn-bottom));border:1px solid #d57f00;
  color:#fff;font-weight:600;font-size:15px;line-height:36px;text-align:center;text-decoration:none;letter-spacing:0.3px}

.testimonials-title{left:40px;top:628px}
.testimonial{position:absolute;left:40px;width:460px}
.rater{font-size:11.5px;color:var(--text-dark);letter-spacing:0.3px;display:flex;align-items:center;gap:5px}
.stars{display:inline-flex;gap:3px}
.stars svg{width:11px;height:11px}
.quote{margin-top:6px;font-size:11px;font-style:italic;font-weight:300;color:var(--text);line-height:16px;letter-spacing:0.3px}
.quote svg{width:10px;height:8px;margin-right:5px;vertical-align:0}
.t-one{top:655px}
.t-two{top:694px}
.t-three{top:755px}

.scrollbar{position:absolute;left:509px;top:118px;width:4px;height:653px;background:#dcd8cf;border-radius:2px}
.scroll-thumb{position:absolute;left:0;top:178px;width:4px;height:201px;background:#8e8a84;border-radius:2px}
</style>
</head>
<body>
<svg width="0" height="0" style="position:absolute">
  <defs>
    <symbol id="star" viewBox="0 0 24 24"><path d="M12 2l2.9 6.9 7.1.6-5.4 4.7 1.6 7.1L12 17.6 5.8 21.3l1.6-7.1L2 9.5l7.1-.6z"/></symbol>
    <symbol id="quote-mark" viewBox="0 0 20 16"><path d="M0 16V9C0 4 2 1 7 0v3C5 4 4 6 4 8h4v8zm11 0V9c0-5 2-8 7-9v3c-2 1-3 3-3 5h4v8z"/></symbol>
  </defs>
</svg>

<section class="cover-side">
  <div class="book-cover">
    <div class="cover-band" role="img" aria-label="Dark red damask patterned band behind the book title"></div>
    <div class="cover-art" role="img" aria-label="Cover scene: a man's silhouette behind prison bars looking out to a tropical beach with palm trees and a woman's legs in fishnet stockings"></div>
    <h1 class="cover-title"><span class="line-one">FLEEING</span><span class="line-two">MARISOL BAY</span></h1>
    <p class="cover-author">HAL BRENNER</p>
  </div>
</section>

<main class="info-side">
  <header class="top-bar">
    <a class="shop-link shop-vantoro" href="#"><span class="label">Buy Now</span><span class="name">vantoro</span></a>
    <a class="shop-link shop-quidlet" href="#"><span class="label">Order Now</span><span class="name">quidlet</span></a>
  </header>

  <div class="photo-frame author-frame"><div class="fill" role="img" aria-label="Portrait photo of the author"></div></div>
  <h2 class="section-title about-title">ABOUT AUTHOR</h2>
  <p class="section-text about-text">Nam libero tempore, cum soluta nobis est eligendi optio cumque nihil impedit quo minus id quod maxime placeat facere possimus, omnis voluptas assumenda est, omnis dolor repellendus. Temporibus autem quibusdam et aut officiis debitis aut rerum necessitatibus saepe eveniet ut et voluptates repudiandae sint et molestiae non recusandae.</p>

  <div class="rule rule-one"></div>

  <div class="photo-frame book-frame"><div class="fill" role="img" aria-label="Hardcover book of Fleeing Marisol Bay"></div></div>
  <h2 class="section-title desc-title">DESCRIPTION OF THE BOOK</h2>
  <p class="section-text desc-text">Nemo enim ipsam voluptatem quia voluptas sit aspernatur aut odit aut fugit, sed quia consequuntur magni dolores eos qui ratione voluptatem sequi nesciunt. Neque porro quisquam est, qui dolorem ipsum quia dolor sit amet, consectetur, adipisci velit, sed quia non numquam eius modi tempora incidunt ut labore et dolore magnam aliquam quaerat voluptatem.</p>
  <a class="read-button" href="#">Read chapter 1</a>

  <div class="rule rule-two"></div>

  <h2 class="section-title testimonials-title">TESTIMONIALS</h2>

  <div class="testimonial t-one">
    <p class="rater">Neil Brown rated it
      <span class="stars">
        <svg fill="var(--star-on)"><use href="#star"/></svg><svg fill="var(--star-on)"><use href="#star"/></svg><svg fill="var(--star-on)"><use href="#star"/></svg><svg fill="var(--star-off)"><use href="#star"/></svg>
      </span></p>
    <p class="quote"><svg fill="#b0aca4"><use href="#quote-mark"/></svg>Quis autem vel eum iure reprehenderit qui in ea voluptate velit esse quam.</p>
  </div>

  <div class="testimonial t-two">
    <p class="rater">John Smith rated it
      <span class="stars">
        <svg fill="var(--star-on)"><use href="#star"/></svg><svg fill="var(--star-on)"><use href="#star"/></svg><svg fill="var(--star-on)"><use href="#star"/></svg><svg fill="var(--star-on)"><use href="#star"/></svg>
      </span></p>
    <p class="quote"><svg fill="#b0aca4"><use href="#quote-mark"/></svg>Consequatur, vel illum qui dolorem eum fugiat quo voluptas nulla pariatur voluptatibus.</p>
  </div>

  <div class="testimonial t-three">
    <p class="rater">Mr,Kevinn rated it
      <span class="stars">
        <svg fill="var(--star-on)"><use href="#star"/></svg><svg fill="var(--star-on)"><use href="#star"/></svg><svg fill="var(--star-on)"><use href="#star"/></svg><svg fill="var(--star-off)"><use href="#star"/></svg>
      </span></p>
    <p class="quote"><svg fill="#b0aca4"><use href="#quote-mark"/></svg>Itaque earum rerum hic tenetur a sapiente delectus, ut aut reiciendis voluptatibus maiores.</p>
  </div>

  <div class="scrollbar"><div class="scroll-thumb"></div></div>
</main>
</body>
</html>
```